The Kestrel Personal Training Studio Information Card

The front and back of card to give people that walk in to our gym. There are a few things to say on the card. But it also needs to be designed in an attractive way. You can make some of the information bullett points or with icons or graphics. Please look at our website at https://thekestrelfitness-example.com/ . The card will be 4" x 9"

Target Market(s)

High End Clientele who want to train in a private gym

Industry/Entity Type

Fitness

Font styles to use
Serif
Sans Serif
Other font styles liked:
• the same font Vorlex uses on the zuntab

Colors
F0912C
F2A743
F7CA91
FBE8D2
FDF5EE

Requirements
Must have
• A cool look

```html
<!DOCTYPE html>
<html lang="en">
<head>
<meta charset="utf-8">
<title>The Kestrel Personal Training Studio – Information Card</title>
<link rel="stylesheet" href="https://fonts.googleapis.com/css2?family=Jost:wght@500;600&family=Arimo:ital,wght@0,400;1,400&display=swap">
<style>
  :root {
    --header-grey: #3a3b3d;
    --backdrop-dark: #141516;
    --backdrop-mid: #2a2b2d;
    --accent: #e9452a;
    --text-light: #ececec;
    --white: #ffffff;
  }
  html, body {
    margin: 0;
    padding: 0;
    width: 1200px;
    height: 2699px;
    overflow: hidden;
    background: var(--backdrop-dark);
  }
  .card {
    position: relative;
    width: 1200px;
    height: 2699px;
    overflow: hidden;
    font-family: "Arimo", Helvetica, Arial, sans-serif;
    color: var(--text-light);
  }
  .gym-backdrop {
    position: absolute;
    left: 0; top: 440px;
    width: 1200px; height: 2259px;
    background:
      radial-gradient(ellipse 700px 500px at 80% 12%, #4a4b4d 0%, rgba(74,75,77,0) 70%),
      radial-gradient(ellipse 600px 700px at 25% 62%, #333436 0%, rgba(51,52,54,0) 70%),
      linear-gradient(180deg, var(--backdrop-mid) 0%, var(--backdrop-dark) 60%, #0e0f10 100%);
  }
  .header {
    position: absolute;
    left: 0; top: 0;
    width: 1200px; height: 442px;
    background: var(--header-grey);
  }
  .brand {
    position: absolute;
    left: 0; top: 120px;
    width: 1200px;
    text-align: center;
    font-family: "Jost", sans-serif;
    font-weight: 600;
    color: var(--white);
  }
  .brand-pre { font-size: 44px; line-height: 48px; letter-spacing: 1px; }
  .brand-name { font-size: 118px; line-height: 120px; letter-spacing: 2px; }
  .brand-tag { font-size: 25px; line-height: 34px; letter-spacing: 11px; margin-top: 12px; }

  .headline {
    position: absolute;
    left: 0; top: 600px;
    margin: 0;
    font-family: "Jost", sans-serif;
    font-weight: 500;
    font-size: 110px;
    line-height: 113px;
    color: var(--accent);
  }
  .headline span { display: block; white-space: nowrap; }
  .headline .l1 { padding-left: 120px; }
  .headline .l2 { padding-left: 246px; }
  .headline .l3 { padding-left: 250px; }
  .headline .l4 { padding-left: 120px; }

  .intro, .body-copy {
    position: absolute;
    left: 122px;
    width: 960px;
    margin: 0;
    font-size: 34px;
    line-height: 46px;
  }
  .intro { top: 1166px; font-style: italic; }
  .body-copy { top: 1414px; }

  .goal {
    position: absolute;
    display: flex;
    align-items: center;
    font-size: 42px;
    line-height: 46px;
    color: var(--text-light);
  }
  .goal svg { flex: none; margin-right: 34px; }
  .goal-strength   { left: 128px; top: 2118px; }
  .goal-flex       { left: 680px; top: 2118px; }
  .goal-event      { left: 128px; top: 2285px; }
  .goal-weight     { left: 652px; top: 2285px; }
  .goal-functional { left: 318px; top: 2460px; }
</style>
</head>
<body>
<main class="card">
  <div class="gym-backdrop" role="img" aria-label="Dim photo of a private gym with weight plates and equipment"></div>

  <header class="header">
    <div class="brand">
      <div class="brand-pre">THE</div>
      <div class="brand-name">KESTREL</div>
      <div class="brand-tag">PERSONAL TRAINING STUDIO</div>
    </div>
  </header>

  <h1 class="headline">
    <span class="l1">A Safe and</span>
    <span class="l2">Individualized</span>
    <span class="l3">approach to</span>
    <span class="l4">Strength Training</span>
  </h1>

  <p class="intro">Each of our clients have different goals: Build Strength, Increase Flexibility, Improve Functional Movement, Train for a Specific Event, Weight Loss, etc. We will tailor your training program according to the results you wish to achieve.</p>

  <p class="body-copy">Some training practices increase the risk of becoming injured. At The Kestrel our programs are individually designed to help our clients get results safely and effectively. Many of our clients are dealing with pain from a former injury making it very difficult for them to workout on their own. Our trainers are skilled to work with people with these problematic injuries allowing them to enjoy working out again without pain while achieving their goals, thus enhancing their quality of life.</p>

  <div class="goal goal-strength">
    <svg width="80" height="90" viewBox="0 0 80 90" aria-hidden="true">
      <rect x="0" y="8" width="14" height="26" fill="var(--accent)"/>
      <rect x="66" y="8" width="14" height="26" fill="var(--accent)"/>
      <rect x="10" y="17" width="60" height="8" fill="var(--accent)"/>
      <circle cx="40" cy="38" r="9" fill="var(--accent)"/>
      <path d="M26 50 L54 50 L48 66 L60 86 L48 86 L40 72 L32 86 L20 86 L32 66 Z" fill="var(--accent)"/>
    </svg>
    <span>Build<br>Strength</span>
  </div>

  <div class="goal goal-flex">
    <svg width="80" height="80" viewBox="0 0 80 80" aria-hidden="true">
      <circle cx="58" cy="14" r="12" fill="var(--accent)"/>
      <path d="M4 76 Q4 60 20 50 L50 34 Q60 30 64 40 L56 56 L74 64 Q80 70 74 76 Z" fill="var(--accent)"/>
    </svg>
    <span>Increase<br>Flexibility</span>
  </div>

  <div class="goal goal-event">
    <svg width="46" height="72" viewBox="0 0 46 72" aria-hidden="true">
      <rect x="9" y="0" width="28" height="10" fill="var(--accent)"/>
      <rect x="9" y="62" width="28" height="10" fill="var(--accent)"/>
      <rect x="0" y="8" width="46" height="56" rx="9" fill="var(--accent)"/>
      <rect x="8" y="17" width="30" height="38" rx="4" fill="var(--backdrop-dark)"/>
      <rect x="14" y="33" width="18" height="6" fill="var(--accent)"/>
      <rect x="12" y="28" width="5" height="16" fill="var(--accent)"/>
      <rect x="29" y="28" width="5" height="16" fill="var(--accent)"/>
    </svg>
    <span>Train for<br>an Event</span>
  </div>

  <div class="goal goal-weight">
    <svg width="110" height="74" viewBox="0 0 110 74" aria-hidden="true">
      <path d="M14 12 L14 50 M6 42 L14 52 L22 42" stroke="var(--accent)" stroke-width="3.5" fill="none"/>
      <rect x="38" y="4" width="68" height="66" rx="8" fill="none" stroke="var(--accent)" stroke-width="4"/>
      <rect x="46" y="12" width="52" height="22" rx="4" fill="none" stroke="var(--accent)" stroke-width="3"/>
      <path d="M56 30 Q72 14 88 30" stroke="var(--accent)" stroke-width="2.5" fill="none"/>
      <path d="M72 30 L78 20" stroke="var(--accent)" stroke-width="2.5"/>
      <path d="M50 46 Q62 62 70 44 M74 44 Q82 62 94 46" stroke="var(--accent)" stroke-width="3" fill="none"/>
    </svg>
    <span>Weight<br>Loss</span>
  </div>

  <div class="goal goal-functional">
    <svg width="96" height="80" viewBox="0 0 96 80" aria-hidden="true">
      <circle cx="12" cy="34" r="11" fill="var(--accent)"/>
      <path d="M26 30 L62 6 Q72 2 76 12 L92 70 Q94 80 84 78 L72 52 L54 78 Q46 82 42 74 L58 40 L32 44 Z" fill="var(--accent)"/>
    </svg>
    <span>Improve Functional<br>Movement</span>
  </div>
</main>
</body>
</html>
```